I am looking for a design that represent my gym/ performance facility that says respect the process on it. This images will be a center piece wall for my gym. I want this wall to stand out. This wall has to be clean and professional. This wall has to be Black and white. The gym is for athletes and regular members so the message has to relate to all. Respect the process represents this wall. Please be creative but clean and professional. Feel free to play with black and white body art. The message again should be "Respect The Process"
THE WALL IS 16FT LONG

Target Market(s)

Fitness and Athletes

Font styles to use
Sans Serif

Requirements
Must have
• Respect The Process
• Must all be in Black and white even images if you use them.
• Motivation words or phrases I.e., "Determination, Focus, Discipline,
• Please use famous or legendary athletes quotes.
• words to use:
• Transformation, Power, success, Strength, Commitment, Motivation, No Excuses, No Regrets, Never Give UP, Beast, Results, Dream Big, Consistency, Hard Work, Challenge,Warrior, Sacrifice, Greatness, Legendary, Winning, Zone, Purpose, Fight, Destiny,
• This Quote will stand alone:
• I HATED EVERY MINUTE OF TRAINING,
• BUT I SAID, "DON'T QUIT.
• SUFFER NOW AND LIVE THE REST
• OF YOUR LIFE A CHAMPION."
• -TOBIAS KRELLEN
• "IF YOU DON'T WANT TO SACRIFICE FOR WHAT YOU WANT
• WHAT YOU WANT BECOMES THE SACRIFICE."
• "EVERYONE HAS THE DESIRE TO WIN, BUT ONLY CHAMPIONS HAVE THE DESIRE TO PREPARE."
• "IT'S ALWAYS SEEMS IMPOSSIBLE UNTIL IT'S DONE."
Nice to have
• It would be nice to have the words in Mustard yellow print as well as the white.T

```html
<!DOCTYPE html>
<html lang="en">
<head>
<meta charset="utf-8">
<title>Respect The Process – Gym Wall</title>
<link rel="stylesheet" href="https://fonts.googleapis.com/css2?family=Bowlby+One&family=Exo+2:ital,wght@1,900&family=Montserrat:wght@400;500;700&display=swap">
<style>
  :root {
    --ink: #1a1a1a;
    --white: #ffffff;
    --mustard: #d8cf2a;
    --panel-top: #d6d6d6;
    --panel-mid: #a9a9a9;
    --panel-low: #7c7c7c;
    --steel-light: #d9d9d9;
    --steel-mid: #6f6f6f;
    --steel-dark: #1c1c1c;
  }
  * { margin: 0; padding: 0; box-sizing: border-box; }
  html, body { width: 917px; height: 1200px; overflow: hidden; background: var(--white); }
  .poster { position: relative; width: 917px; height: 1200px; overflow: hidden; }

  .photo-left {
    position: absolute; left: 0; top: 0; width: 525px; height: 1200px;
    background: linear-gradient(165deg, var(--panel-top) 0%, var(--panel-mid) 40%, var(--panel-low) 70%, var(--panel-mid) 100%);
  }
  .photo-right {
    position: absolute; left: 525px; top: 0; width: 392px; height: 1200px;
    background: linear-gradient(200deg, var(--steel-light) 0%, var(--steel-mid) 25%, var(--steel-dark) 55%, var(--steel-mid) 80%, var(--steel-light) 100%);
  }

  .headline {
    position: absolute; left: 126px; top: 62px;
    font-family: "Bowlby One", sans-serif; font-size: 54px; line-height: 62px;
    color: var(--ink); text-transform: uppercase; letter-spacing: -1px;
  }
  .feature-quote {
    position: absolute; left: 53px; top: 560px;
    font-family: "Bowlby One", sans-serif; font-size: 33px; line-height: 50px;
    color: var(--ink); text-transform: uppercase; letter-spacing: -0.5px;
  }
  .feature-quote .continued {
    display: block; font-size: 18px; line-height: 24px; margin-top: 4px; letter-spacing: 0;
  }
  .feature-quote .attribution {
    display: block; font-family: "Montserrat", sans-serif; font-weight: 700;
    font-size: 14px; line-height: 20px; margin-top: 6px; letter-spacing: 2px; color: var(--white);
  }
  .support-quote {
    position: absolute; left: 53px; top: 808px;
    font-family: "Montserrat", sans-serif; font-weight: 500; font-size: 13.5px; line-height: 16px;
    color: var(--white); text-transform: uppercase; letter-spacing: -0.3px;
  }
  .tag-strip {
    position: absolute; left: 55px; top: 858px; width: 193px; height: 11px;
    background: var(--white); color: var(--ink);
    font-family: "Montserrat", sans-serif; font-weight: 500; font-size: 6px; line-height: 11px;
    letter-spacing: 5.2px; padding-left: 6px; text-transform: uppercase; white-space: nowrap;
  }
  .effort-quote {
    position: absolute; left: 54px; top: 892px;
    font-family: "Exo 2", sans-serif; font-style: italic; font-weight: 900; font-size: 22px; line-height: 29px;
    color: var(--ink); text-transform: uppercase; white-space: pre;
  }
  .effort-quote .soft { text-transform: none; }
  .values {
    position: absolute; left: 52px; top: 1000px;
    font-family: "Montserrat", sans-serif; font-weight: 400; font-size: 19px; line-height: 28px;
    color: var(--white); list-style: none;
  }
  .values li:nth-child(2) { letter-spacing: 3.4px; }
  .values li:nth-child(3) { letter-spacing: 12px; }
</style>
</head>
<body>
<main class="poster">
  <div class="photo-left" role="img" aria-label="Rack of knurled dumbbells in a gym, black and white"></div>
  <div class="photo-right" role="img" aria-label="Close-up of hex dumbbells on a rack in black and white"></div>

  <h1 class="headline">Respect<br>the<br>process</h1>

  <p class="feature-quote">I hated every minute<br>of training,<br>but I said, “don’t quit.
    <span class="continued">Suffer now and live the rest<br>of your life a champion.”</span>
    <span class="attribution">— TOBIAS KRELLEN</span>
  </p>

  <p class="support-quote">Everyone has the desire to win,<br>but only champions have the desire to prepare.</p>

  <div class="tag-strip">Respect the process</div>

  <p class="effort-quote">ALWAYS MAKE <span class="soft">a</span> TOTAL EFFORT ,
EVEN WHEN <span class="soft">the</span> ODDS <span class="soft">are</span>
AGAINST    YOU</p>

  <ul class="values">
    <li>Determination</li>
    <li>Discipline</li>
    <li>Focus</li>
  </ul>
</main>
</body>
</html>
```